Book Cover for Cyber Compliance Book

I need to get a book cover designed for use on "Pagewell Print Portal" - template attached.

The name of the book is: Charting KELMOR

Tagline: A Boardroom Leader’s Field Guide to Oversight and Endurance

Author: Martin J Hollis

Photo of author is attached and a logo for the QBWLN publishing organisation.

Please note: the author is high profile in the cyber security industry and use of his image and name on the book will help online sales.

I am open to changing the amount of copy used on the front and back of the book.

The book is about a European regulation for the financial sector called DORA Digital Operational Resilience Act. It is aimed at corporate level executives within the financial sector and the imagery should include relevant elements such as the EU, Financial sector, digital operations and cybersecurity.

I want to find an imaginative designer than can create something special and appealing.

I am not clear on exactly how many pages will be in the book so the template details may change slightly as the number becomes clear for the width of the spine etc. I will require all the template files used so I can make minor edits in AI or Photoshop

Note I can get the photo and attached logo in higher resolution if required

If possible I would like to see a 3D mockup of the book

Synopsis of Book:

n the ever-evolving landscape of financial services, the Digital Operational Resilience Act (DORA) stands as a beacon of change, ushering in a new era of regulatory requirements aimed at fortifying the digital fortitude of the sector. “Charting KELMOR: A Boardroom Leader’s Field Guide to Oversight and Endurance” is an indispensable guide tailored for leaders who are steering their organisations through the complexities of DORA compliance.
This comprehensive manual delves into the intricacies of DORA, elucidating the rationale behind its inception – the need for a unified and robust approach to managing ICT risks that have become increasingly prevalent in today’s interconnected financial ecosystem. The book offers a granular analysis of the five pillars central to DORA: ICT Risk Management, ICT-related Incident Management, Digital Operational Resilience Testing, ICT Third Party Risk Management, and Information Sharing Arrangements.
For financial entities and ICT service providers operating within the EU and beyond, “Charting KELMOR” serves as a strategic compass. It provides actionable insights into aligning with DORA’s standards, ensuring not just compliance but also a competitive edge in the EU market. The guide highlights the strategic importance of continuous learning and the emergence of specialized roles such as DORA Compliance Specialists, addressing the skills gap and career opportunities within this new regulatory framework.
The book also offers a detailed walkthrough of the Union-wide Oversight Framework, a novel aspect of DORA that places critical ICT third-party providers under direct regulatory scrutiny. It outlines the necessary steps for financial entities to ensure seamless collaboration with these providers, including the integration of specific contractual obligations to uphold DORA’s stringent resilience standards.
With practical advice and real-world scenarios, “Charting KELMOR” equips executives with the knowledge to conduct thorough DORA Compliance Assessments, map dependencies, and engage in scenario testing that aligns with the act’s rigorous testing regimen. It is not just a guide but a strategic tool for proactive adaptation and evolution in the face of DORA’s demands.
As the financial sector navigates these new regulatory waters, “Charting KELMOR” emerges as the quintessential guide for those committed to not just surviving but thriving in the age of digital operational resilience. It is a clarion call for attentiveness, alignment, and preparedness – a must-read for every financial service executive determined to lead their organization with foresight and fortitude.

```html
<!DOCTYPE html>
<html lang="en">
<head>
<meta charset="utf-8">
<title>Charting KELMOR — Cover</title>
<link rel="stylesheet" href="https://fonts.googleapis.com/css2?family=Michroma&family=Montserrat:wght@400;500&display=swap">
<style>
  :root {
    --backdrop: #cfcfcf;
    --navy-deep: #101b2c;
    --navy: #1d3550;
    --steel-blue: #3f7fa6;
    --glow-cyan: #8fd0e4;
    --amber: #d9a15e;
    --bronze: #6a4a30;
    --suit-dark: #1a2638;
    --suit-mid: #2f4560;
    --cream: #f1e9da;
    --spine: #17202f;
  }
  * { box-sizing: border-box; margin: 0; padding: 0; }
  html, body {
    width: 1200px; height: 900px; overflow: hidden;
    background: var(--backdrop);
  }
  .book {
    position: absolute;
    left: 296px; top: 50px;
    width: 608px; height: 800px;
    display: flex;
    box-shadow: 0 12px 30px rgba(0,0,0,0.18);
  }
  .spine {
    position: relative;
    width: 72px; height: 100%;
    background: var(--spine);
    color: var(--cream);
    font-family: "Montserrat", sans-serif;
    font-weight: 400;
  }
  .spine-text {
    position: absolute;
    left: 50%;
    white-space: nowrap;
    font-size: 17px;
    letter-spacing: 0.22em;
    text-transform: uppercase;
    transform: translateX(-50%) rotate(90deg);
    transform-origin: center;
  }
  .spine-title { top: 170px; }
  .spine-author { top: 640px; }

  .front-cover {
    position: relative;
    width: 536px; height: 100%;
    overflow: hidden;
    color: var(--cream);
  }
  .cover-art {
    position: absolute; inset: 0;
    background:
      radial-gradient(ellipse 42% 30% at 72% 42%, rgba(242,200,140,0.75), rgba(217,161,94,0) 70%),
      radial-gradient(ellipse 38% 30% at 30% 40%, rgba(143,208,228,0.55), rgba(143,208,228,0) 70%),
      radial-gradient(ellipse 60% 40% at 60% 85%, rgba(106,74,48,0.6), rgba(106,74,48,0) 75%),
      linear-gradient(160deg, var(--navy-deep) 0%, var(--navy) 28%, var(--steel-blue) 50%, #8a7a66 72%, var(--bronze) 100%);
  }
  .author-portrait {
    position: absolute;
    left: 150px; top: 300px;
    width: 386px; height: 500px;
    border-radius: 46% 46% 0 0 / 28% 28% 0 0;
    background:
      radial-gradient(ellipse 30% 18% at 42% 18%, rgba(120,140,160,0.55), rgba(120,140,160,0) 80%),
      linear-gradient(180deg, var(--suit-mid) 0%, var(--suit-dark) 55%, #241e22 100%);
    opacity: 0.88;
  }
  .tagline {
    position: absolute;
    left: 0; right: 0; top: 128px;
    text-align: center;
    font-family: "Montserrat", sans-serif;
    font-weight: 400;
    font-size: 12px;
    line-height: 1.35;
    letter-spacing: 0.08em;
    text-transform: uppercase;
  }
  .title {
    position: absolute;
    left: 0; right: 0; top: 170px;
    text-align: center;
    font-family: "Michroma", sans-serif;
    font-weight: 400;
    font-size: 50px;
    line-height: 1.1;
    letter-spacing: 0.04em;
    text-transform: uppercase;
  }
  .author-block {
    position: absolute;
    left: 228px; top: 640px;
    font-family: "Montserrat", sans-serif;
    text-transform: uppercase;
  }
  .author-name {
    font-weight: 500;
    font-size: 25px;
    letter-spacing: 0.16em;
  }
  .publisher {
    margin-top: 4px;
    font-weight: 400;
    font-size: 12.5px;
    letter-spacing: 0.1em;
  }
</style>
</head>
<body>
  <div class="book">
    <div class="spine">
      <p class="spine-text spine-title">Charting KELMOR</p>
      <p class="spine-text spine-author">Martin J Hollis</p>
    </div>
    <div class="front-cover">
      <div class="cover-art" role="img" aria-label="Background illustration: glowing cyan digital network lines over a city skyline lit in warm amber light"></div>
      <div class="author-portrait" role="img" aria-label="Photograph of the author in a dark suit and glasses, looking down at a tablet held in both hands"></div>
      <p class="tagline">A Boardroom Leader’s Field Guide<br>to Oversight and Endurance</p>
      <h1 class="title">Charting<br>KELMOR</h1>
      <div class="author-block">
        <p class="author-name">Martin J Hollis</p>
        <p class="publisher">QBWLN Publishing Organisation</p>
      </div>
    </div>
  </div>
</body>
</html>
```